Bold and Enticing Product Packaging - Dog Rolls (wet pet food)

Hello there and welcome to our project! Looking for fun and creative designs for our Dog Rolls (Wet Pet Food Rolls) sold at our butchery retail store.

We are a business located in Papua New Guinea and we manufacture and produce goods that we retail. Our target audience responds better to graphics/visual images rather than reading information - so keep it simple and attractive! Most animals here are working dogs (not leisure pets), so we must focus on this e.g. sell as ‘power for your dog’.

Looking for 2 x designs for each size (1kg & 3kg) – can be the same with different colour schemes/formats or similar. Require to be fully editable in both AI/PSD format.

Packaging dimensions are below. Designs will need to be repeated to fill 1m plastic casing. Note - more colours, more money, keep the colours to a minimum.
1kg product - 1 roll is 11cm wide (length of roll) and 25cm long (wrapped around). 1cm bleed.
3kg product - 1 roll is 16cm wide and 36cm long. 1cm bleed.

Information required (must have):
• 1kg or 3kg
• Real photo of a WORKING DOG (e.g. bullmastiff, doberman, rottweiler, german sheppard) and pet dog
• Brava Tusk logo & “power for your dog” combined... to read “Brava Tusk Power For Your Dog”.
• “Complete nutrition – for all dogs big or small”
• “Pet food only, not for human consumption. Keep refrigerated”

Would be cool (not a must-have) if we could include and be able to interchange the title of flavours (different products) e.g. Original Chunky.

Thank you and look forward to collaborating on some great designs here :)

Target Market(s)

See brief

Font styles to use
Sans Serif

Requirements
Must have
• See brief

```html
<!DOCTYPE html>
<html lang="en">
<head>
<meta charset="utf-8">
<title>Brava Tusk Dog Roll Labels – 1kg and 3kg</title>
<link href="https://fonts.googleapis.com/css2?family=Oswald:wght@500;600&display=swap" rel="stylesheet">
<style>
  :root {
    --board: #9a9a9a;
    --label-bg: #ffffff;
    --ink: #231f20;
    --orange: #ff6a00;
    --purple: #7b0c72;
    --pattern-tone: #f1f1f1;
    --photo-warm: #8a5a34;
    --photo-dark: #1c1512;
  }
  html, body {
    margin: 0;
    width: 1200px;
    height: 959px;
    overflow: hidden;
    background: var(--board);
    font-family: "Oswald", "Arial Narrow", sans-serif;
  }
  .board { position: relative; width: 1200px; height: 959px; }
  .label { position: absolute; display: block; background: var(--label-bg); }
  .label--1kg { left: 248px; top: 83px; width: 699px; height: 299px; }
  .label--3kg { left: 110px; top: 435px; width: 976px; height: 434px; }
  .label text { font-family: "Oswald", "Arial Narrow", sans-serif; }
  .ink { fill: var(--ink); }
  .accent-orange { fill: var(--orange); }
  .accent-purple { fill: var(--purple); }
  .white { fill: #fff; }
</style>
</head>
<body>
<main class="board">

  <!-- 1kg label, orange scheme -->
  <svg class="label label--1kg" viewBox="0 0 699 299" xmlns="http://www.w3.org/2000/svg">
    <defs>
      <linearGradient id="pattern-soft" x1="0" y1="0" x2="1" y2="1">
        <stop offset="0" stop-color="#ffffff"/>
        <stop offset="0.5" stop-color="#f3f3f3"/>
        <stop offset="1" stop-color="#ffffff"/>
      </linearGradient>
      <linearGradient id="photo-tones" x1="0" y1="0" x2="1" y2="0">
        <stop offset="0" stop-color="#9c6a3e"/>
        <stop offset="0.3" stop-color="#e9e2d8"/>
        <stop offset="0.5" stop-color="#3a2418"/>
        <stop offset="1" stop-color="#16110f"/>
      </linearGradient>
      <path id="arc-1kg" d="M359,150 Q478,56 598,150"/>
    </defs>
    <rect class="pattern-field" x="0" y="0" width="699" height="280" fill="url(#pattern-soft)" role="img" aria-label="Faint grey bone and heart pattern"/>
    <rect class="dog-photo" x="0" y="18" width="281" height="262" rx="40" fill="url(#photo-tones)" role="img" aria-label="Photo of a smiling collie beside a panting doberman working dog"/>

    <text class="brand-name accent-orange" x="477" y="66" text-anchor="middle" font-size="30" font-weight="600">Brava Tusk</text>

    <text class="tagline" font-size="27" font-weight="600">
      <textPath href="#arc-1kg" startOffset="50%" text-anchor="middle"><tspan class="accent-orange">POWER</tspan><tspan class="ink"> FOR YOUR </tspan><tspan class="accent-orange">DOG</tspan></textPath>
    </text>

    <polygon class="flavour-brush accent-orange" points="408,142 548,137 542,170 404,174"/>
    <text class="flavour white" x="477" y="165" text-anchor="middle" font-size="19" font-weight="500">CHUNK</text>

    <g class="badge-pet-food">
      <circle cx="304" cy="230" r="23" fill="none" stroke="var(--orange)" stroke-width="1.5"/>
      <circle cx="304" cy="230" r="11" class="accent-orange" role="img" aria-label="Pet food only dog face icon"/>
    </g>
    <g class="badge-not-human">
      <circle cx="364" cy="230" r="23" fill="none" stroke="var(--orange)" stroke-width="1.5"/>
      <circle cx="364" cy="230" r="13" class="accent-orange" role="img" aria-label="Not for human consumption icon"/>
    </g>

    <rect class="dog-silhouettes ink" x="430" y="205" width="84" height="18" rx="6" role="img" aria-label="Silhouettes of a large, medium and small dog"/>
    <text class="accent-orange" x="470" y="243" text-anchor="middle" font-size="12.5" font-weight="500">COMPLETE NUTRITION</text>
    <text class="ink" x="470" y="258" text-anchor="middle" font-size="12.5" font-weight="500">FOR ALL DOGS BIG OR SMALL</text>

    <g class="icon-cold">
      <circle cx="580" cy="230" r="13" class="ink"/>
      <g stroke="#fff" stroke-width="1.4" stroke-linecap="round">
        <line x1="580" y1="222" x2="580" y2="238"/>
        <line x1="573" y1="226" x2="587" y2="234"/>
        <line x1="573" y1="234" x2="587" y2="226"/>
      </g>
    </g>
    <text class="accent-orange" x="637" y="228" text-anchor="middle" font-size="13" font-weight="500">KEEP</text>
    <text class="accent-orange" x="637" y="244" text-anchor="middle" font-size="13" font-weight="500">REFRIGERATED</text>

    <rect class="weight-band accent-orange" x="0" y="279" width="699" height="20"/>
    <text class="white" x="477" y="293.5" text-anchor="middle" font-size="11" font-weight="500">1KG</text>
  </svg>

  <!-- 3kg label, purple scheme -->
  <svg class="label label--3kg" viewBox="0 0 976 434" xmlns="http://www.w3.org/2000/svg">
    <defs>
      <linearGradient id="pattern-soft-3" x1="0" y1="0" x2="1" y2="1">
        <stop offset="0" stop-color="#ffffff"/>
        <stop offset="0.5" stop-color="#f3f3f3"/>
        <stop offset="1" stop-color="#ffffff"/>
      </linearGradient>
      <linearGradient id="photo-tones-3" x1="0" y1="0" x2="1" y2="0">
        <stop offset="0" stop-color="#9c6a3e"/>
        <stop offset="0.3" stop-color="#e9e2d8"/>
        <stop offset="0.5" stop-color="#3a2418"/>
        <stop offset="1" stop-color="#16110f"/>
      </linearGradient>
      <path id="arc-3kg" d="M519,214 Q678,86 839,214"/>
    </defs>
    <rect class="pattern-field" x="0" y="0" width="976" height="407" fill="url(#pattern-soft-3)" role="img" aria-label="Faint grey bone and heart pattern"/>
    <rect class="dog-photo" x="0" y="24" width="394" height="383" rx="50" fill="url(#photo-tones-3)" role="img" aria-label="Photo of a smiling collie beside a panting doberman working dog"/>

    <text class="brand-name accent-purple" x="678" y="104" text-anchor="middle" font-size="42" font-weight="600">Brava Tusk</text>

    <text class="tagline" font-size="38" font-weight="600">
      <textPath href="#arc-3kg" startOffset="50%" text-anchor="middle"><tspan class="accent-purple">POWER</tspan><tspan class="ink"> FOR YOUR </tspan><tspan class="accent-purple">DOG</tspan></textPath>
    </text>

    <polygon class="flavour-brush accent-purple" points="582,205 774,198 768,244 578,249"/>
    <text class="flavour white" x="678" y="237" text-anchor="middle" font-size="26" font-weight="500">CHUNK</text>

    <g class="badge-pet-food">
      <circle cx="446" cy="344" r="31" fill="none" stroke="var(--purple)" stroke-width="2"/>
      <circle cx="446" cy="344" r="15" class="accent-purple" role="img" aria-label="Pet food only dog face icon"/>
    </g>
    <g class="badge-not-human">
      <circle cx="527" cy="344" r="31" fill="none" stroke="var(--purple)" stroke-width="2"/>
      <circle cx="527" cy="344" r="17" class="accent-purple" role="img" aria-label="Not for human consumption icon"/>
    </g>

    <rect class="dog-silhouettes ink" x="614" y="312" width="112" height="24" rx="8" role="img" aria-label="Silhouettes of a large, medium and small dog"/>
    <text class="accent-purple" x="670" y="362" text-anchor="middle" font-size="17" font-weight="500">COMPLETE NUTRITION</text>
    <text class="ink" x="670" y="381" text-anchor="middle" font-size="17" font-weight="500">FOR ALL DOGS BIG OR SMALL</text>

    <g class="icon-cold">
      <circle cx="817" cy="344" r="18" class="ink"/>
      <g stroke="#fff" stroke-width="1.8" stroke-linecap="round">
        <line x1="817" y1="333" x2="817" y2="355"/>
        <line x1="807.5" y1="338.5" x2="826.5" y2="349.5"/>
        <line x1="807.5" y1="349.5" x2="826.5" y2="338.5"/>
      </g>
    </g>
    <text class="accent-purple" x="892" y="341" text-anchor="middle" font-size="18" font-weight="500">KEEP</text>
    <text class="accent-purple" x="892" y="361" text-anchor="middle" font-size="18" font-weight="500">REFRIGERATED</text>

    <rect class="weight-band accent-purple" x="0" y="407" width="976" height="27"/>
    <text class="white" x="678" y="426" text-anchor="middle" font-size="14" font-weight="500">3 KG</text>
  </svg>

</main>
</body>
</html>
```